KelvrasMassage website required

We need a website for a mobile sports massage therapist in the United Kingdom. Specialising in pregnancy and postnatal massage, sports and remedial, deep tissue massage & Corprate Massage. Attached are some logos that we already have in various colours. The file named logo_white_background is what we normally use. Feel free to use the others at your discretion.

Requirements
Must have
• Service areas, Booking system.

```html
<!DOCTYPE html>
<html lang="en">
<head>
<meta charset="utf-8">
<title>Kelvras Massage</title>
<link rel="stylesheet" href="https://fonts.googleapis.com/css2?family=Lato:wght@400;700;900&family=Montserrat:wght@400;600;700&display=swap">
<style>
:root{
  --blue:#4ec0f2;
  --blue-soft:#86d2f6;
  --blue-pale:#c9ebfb;
  --ink:#333333;
  --muted:#6f6f6f;
  --panel:#f1f1f1;
  --grey-band:#7a7a7a;
  --black:#0b0b0b;
  --white:#ffffff;
}
*{box-sizing:border-box;margin:0;padding:0}
html,body{width:1200px;height:4110px;overflow:hidden}
body{font-family:"Lato",sans-serif;color:var(--ink);background:var(--white);position:relative}
.section{position:absolute;left:0;width:1200px}
.btn{display:inline-block;background:var(--blue);color:var(--white);font-family:"Montserrat",sans-serif;font-size:13px;font-weight:600;letter-spacing:.5px;text-transform:uppercase;text-align:center}
.btn-outline{background:var(--white);color:var(--blue);border:1px solid #ddd}
.section-title{font-family:"Montserrat",sans-serif;font-weight:700;font-size:30px;text-transform:uppercase;text-align:center}
.photo{position:absolute}

/* header */
.site-header{top:0;height:137px}
.brand{position:absolute;left:74px;top:34px;font-family:"Lato",sans-serif;font-weight:900;font-size:30px;color:var(--blue);display:flex;align-items:center;gap:10px}
.brand-dot{width:22px;height:22px;border-radius:50%;background:var(--blue)}
.contact-strip{position:absolute;right:110px;top:40px;display:flex;gap:36px;font-size:15px;color:#555}
.contact-strip span{display:flex;align-items:center;gap:8px}
.main-nav{position:absolute;right:110px;top:82px;display:flex;gap:30px;font-family:"Montserrat",sans-serif;font-size:14px;font-weight:600;text-transform:uppercase;color:#444}
.main-nav .active{color:var(--blue)}

/* hero */
.hero{top:137px;height:570px;background:radial-gradient(ellipse at 40% 40%,#2a3a48 0%,#0d1418 55%,#050708 100%)}
.hero-figure{left:200px;top:0;width:560px;height:570px;background:radial-gradient(ellipse at 40% 35%,rgba(200,220,235,.35),rgba(40,80,100,.08) 60%,transparent 75%)}
.hero-title{position:absolute;top:225px;width:100%;text-align:center;font-family:"Montserrat",sans-serif;font-weight:700;font-size:64px;color:var(--white)}
.hero-sub{position:absolute;top:312px;width:100%;text-align:center;font-size:20px;line-height:28px;color:var(--white)}
.hero .btn{position:absolute;left:525px;top:398px;width:210px;height:40px;line-height:40px;border-radius:20px;font-size:14px}
.arrow{position:absolute;top:272px}

/* about */
.about{top:707px;height:477px}
.about .photo{left:173px;top:82px;width:411px;height:312px;background:linear-gradient(135deg,#9bbf6a,#e9ece6 55%,#c4d2b0)}
.about-body{position:absolute;left:616px;top:95px;width:420px}
.about-body .section-title{text-align:left;font-size:30px}
.about-body h3{margin-top:30px;font-family:"Montserrat",sans-serif;color:var(--blue);font-size:22px;line-height:28px;font-weight:600;text-transform:uppercase}
.about-body p{margin-top:18px;font-size:12.5px;line-height:18px;color:var(--muted);text-align:justify}
.about-body .btn{margin-top:22px;width:130px;height:34px;line-height:34px;font-size:11px}

/* coaches */
.coaches{top:1184px;height:537px;background:linear-gradient(180deg,var(--blue-soft),#9ad9f7)}
.coaches .section-title{position:absolute;top:68px;width:100%;color:var(--white)}
.coach{position:absolute;top:150px;width:268px;height:321px;background:var(--white);text-align:center}
.coach .avatar{width:120px;height:120px;border-radius:50%;margin:20px auto 0;background:linear-gradient(180deg,#d8d0c8,#a99a8c)}
.coach h4{margin-top:22px;font-family:"Montserrat",sans-serif;color:var(--blue);font-size:17px;font-weight:600;text-transform:uppercase}
.coach .role{font-size:13px;color:#444;margin-top:2px}
.coach p{margin:12px 22px 0;font-size:11px;line-height:15px;color:var(--muted)}
.socials{display:flex;justify-content:center;gap:6px;margin-top:14px}
.socials i{width:14px;height:14px;border-radius:50%;border:1px solid var(--blue)}

/* services */
.services{top:1721px;height:1361px}
.services .section-title{position:absolute;top:62px;width:100%;color:#444}
.services-intro{position:absolute;top:130px;width:100%;text-align:center;font-size:19px;line-height:28px;color:#555}
.service-row{position:absolute;left:173px;width:860px;height:340px;background:var(--panel)}
.service-row .photo{top:0;width:476px;height:340px}
.service-text{position:absolute;top:0;width:384px;padding:0 14px}
.service-text h3{font-family:"Montserrat",sans-serif;color:var(--blue);font-size:20px;line-height:22px;font-weight:700;text-transform:uppercase}
.service-text p{margin-top:10px;font-size:11.5px;line-height:15.5px;color:var(--muted);text-align:justify}
.service-text .btn{margin-top:22px;width:132px;height:34px;line-height:34px;font-size:11px}
.row-right .photo{left:0}
.row-right .service-text{left:476px}
.row-left .photo{left:384px}
.row-left .service-text{left:0;padding-left:0}

/* blog */
.blog{top:3082px;height:578px;background:var(--grey-band)}
.blog .section-title{position:absolute;top:78px;width:100%;color:var(--white)}
.post{position:absolute;left:173px;width:863px;height:150px}
.post .photo{left:0;top:0;width:172px;height:150px;background:linear-gradient(135deg,#2f3a44,#8b95a0 60%,#c8ccd0)}
.post-body{position:absolute;left:205px;top:0;width:658px}
.post-body p{font-size:17px;line-height:22px;color:var(--white);text-align:justify}
.post-body .btn{margin-top:14px;width:132px;height:34px;line-height:34px;font-size:11px}

/* footer */
.site-footer{top:3660px;height:406px;background:var(--black);color:var(--white)}
.foot-col{position:absolute;top:100px}
.foot-col h5{font-family:"Montserrat",sans-serif;color:var(--blue);font-size:18px;font-weight:700;text-transform:uppercase}
.foot-col ul{list-style:none;margin-top:22px}
.foot-col li{font-size:15px;line-height:32px}
.contact-item{display:flex;gap:14px;margin-top:22px}
.contact-item b{display:block;font-size:14px;text-transform:uppercase}
.contact-item span{font-size:15px;line-height:20px}
.form-field{width:312px;height:36px;background:var(--white);color:#555;font-size:14px;line-height:36px;padding-left:12px;margin-top:10px}
.form-field:first-of-type{margin-top:22px}
.send{margin-top:14px;width:131px;height:38px;line-height:38px;font-size:15px}
.copyright{top:4066px;height:44px;background:var(--blue-soft);color:var(--white);text-align:center;font-size:12px;line-height:44px}
</style>
</head>
<body>

<header class="section site-header">
  <div class="brand"><span class="brand-dot"></span>Kelvras Massage</div>
  <div class="contact-strip">
    <span><svg width="16" height="16" viewBox="0 0 24 24"><path fill="#4ec0f2" d="M6.6 10.8a15.1 15.1 0 0 0 6.6 6.6l2.2-2.2c.3-.3.7-.4 1-.2 1.1.4 2.3.6 3.6.6.6 0 1 .4 1 1V20c0 .6-.4 1-1 1A17 17 0 0 1 3 4c0-.6.4-1 1-1h3.5c.6 0 1 .4 1 1 0 1.3.2 2.5.6 3.6.1.3 0 .7-.2 1z"/></svg>(020) 555 0147</span>
    <span><svg width="18" height="14" viewBox="0 0 18 14"><rect x="1" y="1" width="16" height="12" rx="1" fill="#4ec0f2"/><path d="M1 2l8 6 8-6" stroke="#fff" stroke-width="1.4" fill="none"/></svg>hello@kelvrasmassage.co.uk</span>
  </div>
  <nav class="main-nav">
    <span class="active">Home</span><span>About</span><span>Our Services</span><span>Coaches</span><span>Blog</span><span>Contact Us</span>
  </nav>
</header>

<section class="section hero">
  <div class="photo hero-figure" role="img" aria-label="Wireframe runner in motion over a dark digital background"></div>
  <svg class="arrow" style="left:60px" width="24" height="44" viewBox="0 0 24 44"><path d="M20 2L4 22l16 20" stroke="rgba(255,255,255,.5)" stroke-width="3" fill="none"/></svg>
  <svg class="arrow" style="right:60px" width="24" height="44" viewBox="0 0 24 44"><path d="M4 2l16 20L4 42" stroke="rgba(255,255,255,.5)" stroke-width="3" fill="none"/></svg>
  <h1 class="hero-title">Kelvras Massage</h1>
  <p class="hero-sub">consectetuer adipiscing elit. Aenean commodo ligula eget dolor. Aenean massa.<br>mobile sports massage therapist in the United Kingdom.</p>
  <span class="btn">Make an Appointment</span>
</section>

<section class="section about">
  <div class="photo" role="img" aria-label="Smiling massage therapist in a white uniform outdoors"></div>
  <div class="about-body">
    <h2 class="section-title">About Us</h2>
    <h3>Lorem ipsum dolor sit amet consectetur adipiscing elit.</h3>
    <p>Lorem ipsum dolor sit amet, consectetur adipiscing elit. Quid autem habent admirationis, cum prope accesseris? An hoc usque quaque, aliter in vita? Non igitur de improbo, sed de callido improbo quaerimus, qualis Q. Nam quibus rebus efficiuntur voluptates, eae non sunt in potestate sapientis. Negare non possum. Huic mori optimum esse propter desperationem sapientiae, illi propter spem vivere. Quid enim me prohiberet Epicureum esse, si probarem, quae ille diceret? Qui-vere falsone, quaerere mittimus-dictior osciu as prinesse.</p>
    <span class="btn">More Service</span>
  </div>
</section>

<section class="section coaches">
  <h2 class="section-title">Our Coaches</h2>
  <div class="coach" style="left:173px">
    <div class="avatar" role="img" aria-label="Portrait photo of coach Dorian"></div>
    <h4>Dorian</h4><div class="role">Coach</div>
    <p>Lorem ipsum dolor sit amet, consectetur adipiscing elit. Quid autem habent admirationis, cum prope accesseris? An hoc usque quaque, aliter in vita qualis Q.</p>
    <div class="socials"><i></i><i></i><i></i></div>
  </div>
  <div class="coach" style="left:471px">
    <div class="avatar" role="img" aria-label="Portrait photo of coach Marisol"></div>
    <h4>Marisol</h4><div class="role">Coach</div>
    <p>Lorem ipsum dolor sit amet, consectetur adipiscing elit. Quid autem habent admirationis, cum prope accesseris? An hoc usque quaque, aliter in vita qualis Q.</p>
    <div class="socials"><i></i><i></i><i></i></div>
  </div>
  <div class="coach" style="left:767px">
    <div class="avatar" role="img" aria-label="Portrait photo of coach Elwin"></div>
    <h4>Elwin</h4><div class="role">Coach</div>
    <p>Lorem ipsum dolor sit amet, consectetur adipiscing elit. Quid autem habent admirationis, cum prope accesseris? An hoc usque quaque, aliter in vita qualis Q.</p>
    <div class="socials"><i></i><i></i><i></i></div>
  </div>
</section>

<section class="section services">
  <h2 class="section-title">Our Services</h2>
  <p class="services-intro">Specialising in pregnancy and postnatal massage,<br>sports and remedial, deep tissue massage &amp; Corprate Massage.</p>

  <div class="service-row row-right" style="top:213px">
    <div class="photo" role="img" aria-label="Therapist massaging a pregnant client's belly" style="background:linear-gradient(135deg,#f3ece6,#d9c3b2 55%,#eae3dc)"></div>
    <div class="service-text">
      <h3>Pregnancy &amp;<br>Postnatal Massage</h3>
      <p>Lorem ipsum dolor sit amet, consectetur adipiscing elit. Quid autem habent admirationis, cum prope accesseris? An hoc usque quaque, aliter in vita? Non igitur de improbo, sed de callido improbo quaerimus, qualis Q. Nam quibus rebus efficiuntur voluptates, eae non sunt in potestate sapientis. Negare non possum. Huic mori optimum esse propter desperationem sapientiae, illi propter spem vivere. Quid enim me prohiberet Epicureum esse, si probarem, quae ille diceret? Qui-vere falsone, quaerere mittimus-dictior osciu as prinesse.</p>
      <p>Varietates autem iniusaque fortunae facile veteres philosophorum praeceptis instituta vita superabat. Et quod est munus, quod opus sapientiae? Non modo carum sibi quemque, verum etiam vehementer carum esse? Ta enim iste tenus, hic Stoicorum more nisi novet. Collatio igitur ista te nihil iuvat. Videamus animi partes, quarum est conspectus illustrior.</p>
      <span class="btn">More Service</span>
    </div>
  </div>

  <div class="service-row row-left" style="top:580px">
    <div class="photo" role="img" aria-label="Therapist stretching an athlete's leg on a treatment table" style="background:linear-gradient(135deg,#7a5e4a,#c9b6a4 55%,#eeeae6)"></div>
    <div class="service-text">
      <h3>Sports and<br>Remedial</h3>
      <p>Lorem ipsum dolor sit amet, consectetur adipiscing elit. Quid autem habent admirationis, cum prope accesseris? An hoc usque quaque, aliter in vita? Non igitur de improbo, sed de callido improbo quaerimus, qualis Q. Nam quibus rebus efficiuntur voluptates, eae non sunt in potestate sapientis. Negare non possum. Huic mori optimum esse propter desperationem sapientiae, illi propter spem vivere. Quid enim me prohiberet Epicureum esse, si probarem, quae ille diceret? Qui-vere falsone, quaerere mittimus-dictior osciu as prinesse.</p>
      <p>Varietates autem iniusaque fortunae facile veteres philosophorum praeceptis instituta vita superabat. Et quod est munus, quod opus sapientiae? Non modo carum sibi quemque, verum etiam vehementer carum esse? Ta enim iste tenus, hic Stoicorum more nisi novet. Collatio igitur ista te nihil iuvat. Videamus animi partes, quarum est conspectus illustrior.</p>
      <span class="btn">More Service</span>
    </div>
  </div>

  <div class="service-row row-right" style="top:948px">
    <div class="photo" role="img" aria-label="Therapist applying deep tissue massage to a client's back" style="background:linear-gradient(135deg,#ececec,#c79a80 50%,#f4f2f0)"></div>
    <div class="service-text">
      <h3>Deep Tissue Massage &amp;<br>Corprate Massage.</h3>
      <p>Lorem ipsum dolor sit amet, consectetur adipiscing elit. Quid autem habent admirationis, cum prope accesseris? An hoc usque quaque, aliter in vita? Non igitur de improbo, sed de callido improbo quaerimus, qualis Q. Nam quibus rebus efficiuntur voluptates, eae non sunt in potestate sapientis. Negare non possum. Huic mori optimum esse propter desperationem sapientiae, illi propter spem vivere. Quid enim me prohiberet Epicureum esse, si probarem, quae ille diceret? Qui-vere falsone, quaerere mittimus-dictior osciu as prinesse.</p>
      <p>Varietates autem iniusaque fortunae facile veteres philosophorum praeceptis instituta vita superabat. Et quod est munus, quod opus sapientiae? Non modo carum sibi quemque, verum etiam vehementer carum esse? Ta enim iste tenus, hic Stoicorum more nisi novet. Collatio igitur ista te nihil iuvat. Videamus animi partes, quarum est conspectus illustrior.</p>
      <span class="btn">More Service</span>
    </div>
  </div>
</section>

<section class="section blog">
  <h2 class="section-title">Blog Posts</h2>
  <article class="post" style="top:157px">
    <div class="photo" role="img" aria-label="Athlete receiving a sports massage"></div>
    <div class="post-body">
      <p>Lorem ipsum dolor sit amet, consectetur adipiscing elit. Quid autem habent admirationis, cum prope accesseris? An hoc usque quaque, aliter in vita? Non igitur de improbo, sed de callido improbo quaerimus, qualis Q. Nam quibus rebus efficiuntur voluptates, eae non sunt in potestate sapientis. Negare non possum. Huic mori optimum esse propter desperationemQui-vere</p>
      <span class="btn btn-outline">More Service</span>
    </div>
  </article>
  <article class="post" style="top:348px">
    <div class="photo" role="img" aria-label="Therapist treating a client's leg in a studio"></div>
    <div class="post-body">
      <p>Lorem ipsum dolor sit amet, consectetur adipiscing elit. Quid autem habent admirationis, cum prope accesseris? An hoc usque quaque, aliter in vita? Non igitur de improbo, sed de callido improbo quaerimus, qualis Q. Nam quibus rebus efficiuntur voluptates, eae non sunt in potestate sapientis. Negare non possum. Huic mori optimum esse propter desperationemQui-vere</p>
      <span class="btn btn-outline">More Service</span>
    </div>
  </article>
</section>

<footer class="section site-footer">
  <div class="foot-col" style="left:85px">
    <h5>Contact Us</h5>
    <div class="contact-item">
      <svg width="22" height="30" viewBox="0 0 22 30"><path d="M11 0a11 11 0 0 0-11 11c0 8 11 19 11 19s11-11 11-19A11 11 0 0 0 11 0z" fill="#4ec0f2"/><circle cx="11" cy="11" r="4.5" fill="#0b0b0b"/></svg>
      <div><b>Address</b><span>42 Harbour Row<br>Brislow, BR4 7QT</span></div>
    </div>
    <div class="contact-item">
      <svg width="22" height="22" viewBox="0 0 24 24"><path fill="#4ec0f2" d="M6.6 10.8a15.1 15.1 0 0 0 6.6 6.6l2.2-2.2c.3-.3.7-.4 1-.2 1.1.4 2.3.6 3.6.6.6 0 1 .4 1 1V20c0 .6-.4 1-1 1A17 17 0 0 1 3 4c0-.6.4-1 1-1h3.5c.6 0 1 .4 1 1 0 1.3.2 2.5.6 3.6.1.3 0 .7-.2 1z"/></svg>
      <div><b>Phone Number</b><span>020 555 0193</span></div>
    </div>
  </div>
  <div class="foot-col" style="left:381px">
    <h5>About</h5>
    <ul><li>Home</li><li>About Us</li><li>Services</li><li>Help us</li></ul>
  </div>
  <div class="foot-col" style="left:559px">
    <h5>Resources</h5>
    <ul><li>Support</li><li>Why Us</li><li>Testimonials</li><li>FAQ</li></ul>
  </div>
  <div class="foot-col" style="left:786px">
    <h5>Get in Touch</h5>
    <div class="form-field">Your Name</div>
    <div class="form-field">Email address</div>
    <div class="form-field">Phone</div>
    <div class="btn send">Send</div>
  </div>
</footer>
<div class="section copyright">© 2018 Kelvras Massage All Right Reserved</div>

</body>
</html>
```